Husband and i just started a new Hotshot trucking company, Its a pick up and delivery service. We own our own 40 foot gooseneck trailer... Called Roadbird Hauling LLC. We are needing some business cards made to help advertise our new company. We are based out of Ft Worth Tx. We are the ones who transports what ever loads to where ever they need to go, at any time. We stride for success. And we wont take no for an answer.
What we need on there is the following: need it to be all caps please.

DOUGLAS PRATHER "BO"
555-318-4426
ROADBIRDHAULINGLLC@MAILNEST.EXAMPLE

SHELBY CORWIN
555-604-7153

We have a couple logos already made. however we are always game to see new ideas. Thank you for your time.

Target Market(s)

Youth, middle aged. Home buyers

Industry/Entity Type

Hotshot Trucking Pick up and Delivery Service

Contact Information for Business Card

DOUGLAS PRATHER "BO" 555-318-4426 ROADBIRDHAULINGLLC@MAILNEST.EXAMPLE SHELBY CORWIN 555-604-7153 ROADBIRDHAULINGLLC@MAILNEST.EXAMPLE

Font styles to use
Serif
Script

Colors
0054AA
0677BA
7BADD7
CADEEF
E8F1F8
0094D4
00A9DD
6FCCEA
C7EBF8
E9F6FB

Requirements
Must have
• Our company logo. and look one of a kind. also has to be able to catch some ones eye and stand out
Nice to have
• open for ideas..

```html
<!DOCTYPE html>
<html lang="en">
<head>
<meta charset="utf-8">
<title>Roadbird Hauling LLC — Business Card</title>
<link rel="stylesheet" href="https://fonts.googleapis.com/css2?family=Poppins:wght@400;600;700&display=swap">
<style>
  :root {
    --page-bg: #e6e8ec;
    --card-top: #f3f1f2;
    --accent-stripe: #3aa3ea;
    --navy: #1c2a55;
    --name-white: #ffffff;
    --detail-grey: #c9cfdb;
    --brand-navy: #1c2a55;
    --brand-blue: #0677ba;
  }
  html, body {
    margin: 0;
    width: 1200px;
    height: 900px;
    overflow: hidden;
    background: var(--page-bg);
    font-family: "Poppins", sans-serif;
  }
  .business-card {
    position: absolute;
    left: 100px;
    top: 140px;
    width: 1000px;
    height: 620px;
    background: var(--card-top);
    box-shadow: 0 10px 30px rgba(20, 30, 60, 0.18);
    overflow: hidden;
  }
  .brand-area {
    position: absolute;
    left: 0;
    top: 0;
    width: 100%;
    height: 357px;
    display: flex;
    align-items: center;
    justify-content: center;
  }
  .brand-name {
    margin: 0;
    font-weight: 700;
    font-size: 50px;
    letter-spacing: 1px;
    color: var(--brand-navy);
  }
  .accent-stripe {
    position: absolute;
    left: 0;
    top: 357px;
    width: 100%;
    height: 13px;
    background: var(--accent-stripe);
  }
  .contact-band {
    position: absolute;
    left: 0;
    top: 370px;
    width: 100%;
    height: 250px;
    background: var(--navy);
  }
  .contact {
    position: absolute;
    top: 46px;
  }
  .contact--left {
    right: 536px;
    text-align: right;
  }
  .contact--right {
    left: 522px;
    text-align: left;
  }
  .contact-name {
    margin: 0;
    font-weight: 600;
    font-size: 38px;
    line-height: 46px;
    color: var(--name-white);
  }
  .contact-phone {
    margin: 8px 0 0;
    font-weight: 400;
    font-size: 28px;
    line-height: 36px;
    color: var(--detail-grey);
  }
  .contact-email {
    margin: 2px 0 0;
    font-weight: 400;
    font-size: 16px;
    line-height: 24px;
    color: var(--detail-grey);
  }
  .contact-divider {
    position: absolute;
    left: 491px;
    top: 52px;
    width: 3px;
    height: 117px;
    background: var(--name-white);
  }
</style>
</head>
<body>
  <div class="business-card">
    <div class="brand-area">
      <p class="brand-name">ROADBIRD HAULING LLC</p>
    </div>
    <div class="accent-stripe"></div>
    <div class="contact-band">
      <div class="contact contact--left">
        <p class="contact-name">SHELBY CORWIN</p>
        <p class="contact-phone">555-604-7153</p>
        <p class="contact-email">ROADBIRDHAULINGLLC@MAILNEST.EXAMPLE</p>
      </div>
      <div class="contact-divider"></div>
      <div class="contact contact--right">
        <p class="contact-name">DOUGLAS PRATHER "BO"</p>
        <p class="contact-phone">555-318-4426</p>
        <p class="contact-email">ROADBIRDHAULINGLLC@MAILNEST.EXAMPLE</p>
      </div>
    </div>
  </div>
</body>
</html>
```